Boutique Financial Services/Advisor Business Needs Web Design

Looking for an informational and functional web design for my Financial Services/Financial Advisement business. It should have functionality for Company name, address, phone #, "About Us", Who we are, Our Mission, Services we offer, Biographies/Photos of/about "The Team", and possibly a link to "Contact Us". Would like to see something new & exciting blended with a traditional/professional look that will appeal to those approaching retirement, as well as those younger clients that are beginning to think about planning for the future. I already have a web domain through HostMeadow, but would like this to be the design we use for that domain.
Financial Services/Financial Advisor
Coded - Design and coding required
1 page

```html
<!DOCTYPE html>
<html lang="en">
<head>
<meta charset="utf-8">
<title>Crestline Wealth Management</title>
<link href="https://fonts.googleapis.com/css2?family=Cinzel:wght@400;500;600&family=Raleway:wght@400;500;600;700&family=Lato:wght@400;700&display=swap" rel="stylesheet">
<style>
:root{
  --navy:#0b0d52;
  --navy-deep:#070940;
  --blue:#0c5db5;
  --blue-soft:#5c9bd6;
  --pale:#e7eff8;
  --sky:#e3f3fb;
  --ink:#1d1d2b;
  --text:#3a3a48;
  --grey:#8a8f9c;
  --white:#ffffff;
  --gold:#f6b40e;
}
*{box-sizing:border-box;margin:0;padding:0}
html,body{width:1200px;height:4422px;overflow:hidden}
body{position:relative;font-family:"Lato",sans-serif;color:var(--text);background:var(--white)}
.abs{position:absolute}
section,header,footer{position:absolute;left:0;width:1200px;overflow:hidden}
.btn-solid{position:absolute;display:flex;align-items:center;justify-content:center;background:var(--blue);color:#fff;font-size:12px;letter-spacing:.3px;border-radius:5px;font-family:"Raleway",sans-serif;font-weight:500}
.btn-line{position:absolute;display:flex;align-items:center;justify-content:center;border:2px solid var(--blue-soft);color:var(--blue-soft);font-size:12px;font-family:"Raleway",sans-serif;font-weight:500;background:#fff}
.ph{position:absolute}

/* header */
.site-header{top:0;height:118px;background:#fff;border-top:5px solid var(--blue)}
.brand{position:absolute;left:142px;top:58px;width:180px;text-align:center;color:var(--navy)}
.brand-name{font-family:"Cinzel",serif;font-size:17px;line-height:17px}
.brand-sub{font-family:"Cinzel",serif;font-size:14px;color:var(--grey);line-height:15px}
.nav{position:absolute;top:52px;font-size:12px;color:var(--ink)}

/* hero */
.hero{top:118px;height:493px;background:var(--pale)}
.hero h1{position:absolute;left:142px;top:112px;font-family:"Cinzel",serif;font-weight:500;font-size:48px;line-height:52px;color:var(--navy);letter-spacing:1px}
.hero-sub{position:absolute;left:143px;top:282px;font-size:13.5px;color:var(--ink)}

/* about */
.about{top:611px;height:490px;background:var(--pale)}
.eyebrow{position:absolute;left:683px;top:80px;font-family:"Raleway",sans-serif;font-size:19px;font-weight:500;color:var(--blue)}
.about-title{position:absolute;left:683px;top:104px;font-family:"Cinzel",serif;font-size:33px;line-height:40px;color:var(--navy)}
.about-title span{color:var(--grey)}
.rule{position:absolute;height:4px;background:var(--blue)}
.para{font-size:12.5px;line-height:21.5px;color:var(--ink)}

/* services */
.services{top:1099px;height:1231px;background:var(--pale)}
.section-title{position:absolute;left:0;width:1200px;text-align:center;font-family:"Cinzel",serif;font-size:35px;color:var(--navy);letter-spacing:1px}
.card-bg{position:absolute;width:320px;height:320px;background:#fff;transform:rotate(45deg);box-shadow:0 10px 28px rgba(30,50,100,.12)}
.card-icon{position:absolute;width:86px;height:86px;background:var(--blue);transform:rotate(45deg)}
.card-title{position:absolute;width:320px;text-align:center;font-family:"Raleway",sans-serif;font-weight:600;font-size:19px;color:var(--ink)}
.card-text{position:absolute;width:300px;text-align:center;font-size:12.5px;line-height:21.7px;color:var(--ink)}

/* team */
.team{top:2330px;height:577px;background:radial-gradient(ellipse at 50% 60%,#16307a 0%,var(--navy) 55%,var(--navy-deep) 100%)}
.member-name{position:absolute;width:300px;text-align:center;font-family:"Raleway",sans-serif;font-size:19px;font-weight:500;color:#fff}
.member-text{position:absolute;width:300px;text-align:center;font-size:12px;line-height:21px;color:#d6dbef}
.member-link{position:absolute;width:300px;text-align:center;font-size:12px;color:#8fb4ea;text-decoration:underline;letter-spacing:.3px}

/* testimonials */
.testimonials{top:2907px;height:608px;background:#fff}
.t-card{position:absolute;top:175px;width:439px;height:287px;border:1px solid #e3e6ec;background:#fff}
.t-text{position:absolute;left:22px;top:78px;width:396px;font-size:12.5px;line-height:21.6px;color:var(--text)}
.t-name{position:absolute;left:96px;top:212px;font-family:"Raleway",sans-serif;font-weight:600;font-size:14.5px;color:var(--ink)}
.t-role{position:absolute;left:96px;top:234px;font-size:13px;color:var(--text)}

/* inquiry */
.inquiry{top:3515px;height:529px;background:var(--sky)}
.field{position:absolute;height:38px;background:#fff;border:1px solid #d9dde4;font-size:11px;color:#555}
.field .ic{position:absolute;left:0;top:0;width:34px;height:100%;border-right:1px solid #e1e4ea;display:flex;align-items:center;justify-content:center}
.field .lbl{position:absolute;left:46px;top:12px}

/* footer */
.site-footer{top:4044px;height:378px;background:var(--navy)}
.f-nav{position:absolute;top:170px;font-size:12px;color:#fff}
.f-label{position:absolute;font-size:11px;color:#fff;font-weight:700}
.f-value{position:absolute;font-size:13px;color:#fff;white-space:nowrap}
.f-diamond{position:absolute;width:38px;height:38px;background:#2a2d6e;transform:rotate(45deg)}
.social{position:absolute;top:330px;width:27px;height:27px;border:1px solid #fff}
</style>
</head>
<body>

<header class="site-header">
  <div class="brand">
    <div class="brand-name">CRESTLINE WEALTH</div>
    <div class="brand-sub">MANAGEMENT</div>
  </div>
  <nav>
    <span class="nav" style="left:645px">Home</span>
    <span class="nav" style="left:709px">About Us</span>
    <span class="nav" style="left:788px">Services</span>
    <span class="nav" style="left:862px">Our Team</span>
  </nav>
  <div class="btn-solid" style="left:946px;top:36px;width:112px;height:40px">CONTACT US</div>
</header>

<section class="hero">
  <svg class="abs" style="left:0;top:0" width="1200" height="493">
    <defs>
      <linearGradient id="heroPhoto" x1="0" y1="0" x2="1" y2="1">
        <stop offset="0" stop-color="#3a4658"/>
        <stop offset=".45" stop-color="#c9ced6"/>
        <stop offset="1" stop-color="#e9edf2"/>
      </linearGradient>
    </defs>
    <polygon points="498,0 1200,0 1200,493 850,493" fill="url(#heroPhoto)" role="img" aria-label="Photo of advisors reviewing financial charts on paper at a desk"/>
    <polygon points="498,0 512,0 864,493 850,493" fill="var(--blue)"/>
  </svg>
  <h1>PLANNING YOUR<br>FUTURE WITH<br>CONFIDENCE</h1>
  <div class="hero-sub">Achieving Your Financial Goals through Expert Wealth Management</div>
  <div class="btn-solid" style="left:141px;top:334px;width:113px;height:38px">GET STARTED</div>
</section>

<section class="about">
  <div class="abs" style="left:140px;top:74px;width:42px;height:42px;background:var(--blue);transform:rotate(45deg)"></div>
  <div class="abs" style="left:178px;top:70px;width:20px;height:20px;background:var(--blue);transform:rotate(45deg)"></div>
  <div class="abs" style="left:221px;top:239px;width:2px;height:228px;background:#8b9ec0"></div>
  <div class="abs" style="left:221px;top:465px;width:88px;height:2px;background:#8b9ec0"></div>
  <div class="abs" style="left:263px;top:67px;width:118px;height:65px;background:#7aa8dc;text-align:center;color:var(--blue)">
    <div style="font-family:Raleway,sans-serif;font-weight:700;font-size:27px;line-height:30px;margin-top:4px">22+</div>
    <div style="font-size:10px;line-height:11px">YEARS<br>EXPERIENCE</div>
  </div>
  <div class="ph" role="img" aria-label="Photo of an advisor's hands working with a calculator and documents" style="left:240px;top:144px;width:141px;height:303px;background:linear-gradient(160deg,#5a6475,#c6ccd6 60%,#eef1f4)"></div>
  <div class="ph" role="img" aria-label="Photo of a client meeting around a table with reports" style="left:388px;top:69px;width:237px;height:305px;background:linear-gradient(150deg,#4a4e55,#9ea6b0 50%,#dfe4ea)"></div>
  <div class="ph" role="img" aria-label="Brochure mockup with the firm's name on the cover" style="left:501px;top:230px;width:134px;height:232px;background:linear-gradient(100deg,#8d96a3,#f5f7fa 30%,#ffffff 70%,#1d56a2)"></div>

  <div class="eyebrow">WHO WE ARE</div>
  <div class="about-title">CRESTLINE WEALTH<br><span>MANAGEMENT</span></div>
  <div class="rule" style="left:683px;top:192px;width:70px"></div>
  <p class="para abs" style="left:683px;top:216px;width:376px">Lorem ipsum dolor sit amet, consectetuer adipiscing elit, sed diam nonummy nibh euismod tincidunt ut laoreet dolor magna aliquam erat volutpat. Ut wisi enim ad minim veni quis nostrud exerci tation ullamcorper suscipit lobortis.</p>
  <svg class="abs" style="left:683px;top:320px" width="38" height="38" viewBox="0 0 38 38" fill="none" stroke="var(--navy)" stroke-width="1.6">
    <path d="M2 36 L16 14 L24 26 L28 20 L36 36 Z"/><path d="M16 14 V2 H26 L23 5 L26 8 H16"/>
  </svg>
  <div class="abs" style="left:737px;top:318px;font-family:Raleway,sans-serif;font-weight:600;font-size:13px;color:var(--ink)">Our Mission</div>
  <p class="abs" style="left:737px;top:336px;width:320px;font-size:11px;line-height:18px;color:var(--ink)">Lorem ipsum dolor sit amet, consectetuer adipiscing elit, sed diam nonummy nibh euismod tincidunt.</p>
  <div class="btn-solid" style="left:683px;top:399px;width:127px;height:39px;background:var(--blue-soft);border-radius:0">CONTACT US</div>
</section>

<section class="services">
  <svg class="abs" style="left:0;top:0" width="1200" height="1231">
    <polygon points="1200,0 1200,560 860,340 1040,0" fill="#eef4fa"/>
    <polygon points="0,240 330,700 0,1100" fill="#edf3fa"/>
    <polygon points="700,1231 1200,700 1200,1231" fill="#eef4fa"/>
  </svg>
  <div class="section-title" style="top:56px">OUR SERVICES</div>
  <div class="rule" style="left:566px;top:108px;width:68px"></div>

  <div class="card-bg" style="left:223px;top:217px"></div>
  <div class="card-bg" style="left:577px;top:377px"></div>
  <div class="card-bg" style="left:316px;top:631px"></div>
  <div class="card-bg" style="left:661px;top:804px"></div>

  <div class="card-icon" style="left:340px;top:158px"></div>
  <div class="card-icon" style="left:694px;top:317px"></div>
  <div class="card-icon" style="left:433px;top:580px"></div>
  <div class="card-icon" style="left:778px;top:754px"></div>
  <svg class="abs" style="left:363px;top:181px" width="40" height="40" viewBox="0 0 40 40" fill="none" stroke="#fff" stroke-width="1.8"><rect x="6" y="22" width="20" height="12"/><path d="M6 22 V10 H12 V22"/><circle cx="28" cy="10" r="7"/><path d="M28 6 V14"/></svg>
  <svg class="abs" style="left:717px;top:340px" width="40" height="40" viewBox="0 0 40 40" fill="none" stroke="#fff" stroke-width="1.8"><circle cx="20" cy="20" r="15"/><circle cx="20" cy="20" r="8"/><path d="M20 15 V25 M17 18 H22 M18 22 H23"/></svg>
  <svg class="abs" style="left:456px;top:603px" width="40" height="40" viewBox="0 0 40 40" fill="none" stroke="#fff" stroke-width="1.8"><path d="M14 34 V24 M20 34 V18 M26 34 V12 M32 34 V8"/><path d="M6 26 L16 16 L22 20 L34 6"/><circle cx="9" cy="30" r="5"/></svg>
  <svg class="abs" style="left:801px;top:777px" width="40" height="40" viewBox="0 0 40 40" fill="none" stroke="#fff" stroke-width="1.8"><circle cx="20" cy="20" r="14" stroke-dasharray="4 3"/><circle cx="20" cy="16" r="4"/><path d="M12 28 C14 22 26 22 28 28"/></svg>

  <div class="card-title" style="left:223px;top:288px">Retirement Planning</div>
  <p class="card-text" style="left:233px;top:324px">Lorem ipsum dolor sit amet, consectetuer adipiscing elit, sed diam nonummy nibh euismod tincidunt ut laoreet dolor magna aliquam erat volutpat. Ut wisi enim ad minim veni quis nostrud exerci tation ullamcorper suscipit lobortis.</p>
  <div class="btn-line" style="left:319px;top:455px;width:127px;height:41px">CONTACT US</div>

  <div class="card-title" style="left:577px;top:448px">Investment Strategies</div>
  <p class="card-text" style="left:587px;top:484px">Lorem ipsum dolor sit amet, consectetuer adipiscing elit, sed diam nonummy nibh euismod tincidunt ut laoreet dolor magna aliquam erat volutpat. Ut wisi enim ad minim veni quis nostrud exerci tation ullamcorper suscipit lobortis.</p>
  <div class="btn-line" style="left:673px;top:614px;width:127px;height:41px">CONTACT US</div>

  <div class="card-title" style="left:316px;top:709px">Wealth Management</div>
  <p class="card-text" style="left:326px;top:745px">Lorem ipsum dolor sit amet, consectetuer adipiscing elit, sed diam nonummy nibh euismod tincidunt ut laoreet dolor magna aliquam erat volutpat. Ut wisi enim ad minim veni quis nostrud exerci tation ullamcorper suscipit lobortis.</p>
  <div class="btn-line" style="left:412px;top:876px;width:127px;height:41px">CONTACT US</div>

  <div class="card-title" style="left:661px;top:882px">Executive Leadership</div>
  <p class="card-text" style="left:671px;top:919px">Lorem ipsum dolor sit amet, consectetuer adipiscing elit, sed diam nonummy nibh euismod tincidunt ut laoreet dolor magna aliquam erat volutpat. Ut wisi enim ad minim veni quis nostrud exerci tation ullamcorper suscipit lobortis.</p>
  <div class="btn-line" style="left:757px;top:1049px;width:127px;height:41px">CONTACT US</div>
</section>

<section class="team">
  <svg class="abs" style="left:0;top:0" width="1200" height="577">
    <polygon points="1095,130 1200,75 1200,325" fill="var(--blue)"/>
    <line x1="1090" y1="150" x2="1200" y2="330" stroke="#2c4f9c" stroke-width="1"/>
  </svg>
  <div class="section-title" style="top:83px;color:#fff">MEET THE TEAM</div>
  <div class="rule" style="left:566px;top:135px;width:68px;background:#fff"></div>

  <svg class="abs" style="left:0;top:155px" width="1200" height="230" fill="none" stroke="#6e8ad0" stroke-width="1">
    <polygon points="288,15 388,115 288,215 188,115"/>
    <polygon points="599,15 699,115 599,215 499,115"/>
    <polygon points="910,15 1010,115 910,215 810,115"/>
  </svg>
  <div class="ph" role="img" aria-label="Portrait photo of team member Aaron Mitchell" style="left:220px;top:196px;width:137px;height:141px;background:linear-gradient(#e4e6ea,#9aa3b2)"></div>
  <div class="ph" role="img" aria-label="Portrait photo of team member Nadia Brooks" style="left:531px;top:196px;width:137px;height:141px;background:linear-gradient(#dfe2e6,#b9bec6)"></div>
  <div class="ph" role="img" aria-label="Portrait photo of team member Owen Carter" style="left:842px;top:196px;width:137px;height:141px;background:linear-gradient(#e6e8ec,#a5acb8)"></div>

  <div class="member-name" style="left:138px;top:384px">Aaron Mitchell</div>
  <div class="member-name" style="left:449px;top:384px">Nadia Brooks</div>
  <div class="member-name" style="left:760px;top:384px">Owen Carter</div>
  <p class="member-text" style="left:138px;top:415px">Lorem ipsum dolor sit amet consectetuer adipiscing elit sed diam nonum.</p>
  <p class="member-text" style="left:449px;top:415px">Lorem ipsum dolor sit amet consectetuer adipiscing elit sed diam nonum.</p>
  <p class="member-text" style="left:760px;top:415px">Lorem ipsum dolor sit amet consectetuer adipiscing elit sed diam nonum.</p>
  <div class="member-link" style="left:138px;top:473px">MORE INFORMATION</div>
  <div class="member-link" style="left:449px;top:473px">MORE INFORMATION</div>
  <div class="member-link" style="left:760px;top:473px">MORE INFORMATION</div>
</section>

<section class="testimonials">
  <div class="section-title" style="top:86px">CLIENT TESTIMONIALS</div>
  <div class="rule" style="left:566px;top:138px;width:68px"></div>

  <div class="t-card" style="left:141px">
    <svg class="abs" style="left:22px;top:28px" width="42" height="30" viewBox="0 0 42 30" fill="var(--blue)"><path d="M0 30 V16 C0 6 6 1 16 0 V6 C10 7 8 10 8 14 H16 V30 Z M22 30 V16 C22 6 28 1 38 0 V6 C32 7 30 10 30 14 H38 V30 Z"/></svg>
    <div class="abs" style="left:316px;top:28px;color:var(--gold);font-size:17px;letter-spacing:4px">★★★★★</div>
    <p class="t-text">Lorem ipsum dolor sit amet, consectetuer adipiscin elit sed diam nonummy nibh euismod tincidunt ut laoreet dolore magna aliquam erat volutpat. Ut wisi enim ad minim veniam, quis nostrud exerci tation ullamcorper suscipit lobortis nisl ut aliquip ex ea commodo.</p>
    <div class="ph" role="img" aria-label="Client photo" style="left:24px;top:207px;width:62px;height:62px;border-radius:50%;background:linear-gradient(#d9dde3,#8e97a6)"></div>
    <div class="t-name">Martin Hale</div>
    <div class="t-role">Aliquam Erat</div>
  </div>
  <div class="t-card" style="left:618px">
    <svg class="abs" style="left:22px;top:28px" width="42" height="30" viewBox="0 0 42 30" fill="var(--blue)"><path d="M0 30 V16 C0 6 6 1 16 0 V6 C10 7 8 10 8 14 H16 V30 Z M22 30 V16 C22 6 28 1 38 0 V6 C32 7 30 10 30 14 H38 V30 Z"/></svg>
    <div class="abs" style="left:316px;top:28px;color:var(--gold);font-size:17px;letter-spacing:4px">★★★★★</div>
    <p class="t-text">Lorem ipsum dolor sit amet, consectetuer adipiscin elit sed diam nonummy nibh euismod tincidunt ut laoreet dolore magna aliquam erat volutpat. Ut wisi enim ad minim veniam, quis nostrud exerci tation ullamcorper suscipit lobortis nisl ut aliquip ex ea commodo.</p>
    <div class="ph" role="img" aria-label="Client photo" style="left:24px;top:207px;width:62px;height:62px;border-radius:50%;background:linear-gradient(#e2e4e8,#a8a3a0)"></div>
    <div class="t-name">Lena Ward</div>
    <div class="t-role">Aliquam Erat</div>
  </div>

  <svg class="abs" style="left:550px;top:500px" width="100" height="20" viewBox="0 0 100 20" fill="none">
    <path d="M24 10 H4 M10 4 L4 10 L10 16" stroke="#b9c2cf" stroke-width="1.5"/>
    <circle cx="34" cy="10" r="1.6" fill="#b9c2cf"/><circle cx="44" cy="10" r="1.8" fill="var(--navy)"/><circle cx="54" cy="10" r="1.6" fill="#b9c2cf"/><circle cx="64" cy="10" r="1.6" fill="#b9c2cf"/>
    <path d="M72 10 H96 M90 4 L96 10 L90 16" stroke="var(--blue)" stroke-width="2"/>
  </svg>
</section>

<section class="inquiry">
  <svg class="abs" style="left:0;top:0" width="1200" height="529">
    <polygon points="0,300 0,529 200,529" fill="#fff"/>
    <polygon points="1200,40 1200,529 660,529" fill="#fff"/>
    <polygon points="0,0 420,0 0,260" fill="#eaf6fc"/>
  </svg>
  <div class="section-title" style="top:92px">QUICK INQUIRY</div>
  <div class="rule" style="left:566px;top:144px;width:68px"></div>

  <div class="field" style="left:304px;top:173px;width:287px"><div class="ic"><svg width="12" height="12" viewBox="0 0 12 12" fill="var(--blue)"><circle cx="6" cy="3.5" r="3"/><path d="M0 12 C0 7 12 7 12 12Z"/></svg></div><span class="lbl">First Name*</span></div>
  <div class="field" style="left:608px;top:173px;width:287px"><div class="ic"><svg width="12" height="12" viewBox="0 0 12 12" fill="var(--blue)"><circle cx="6" cy="3.5" r="3"/><path d="M0 12 C0 7 12 7 12 12Z"/></svg></div><span class="lbl">Last Name*</span></div>
  <div class="field" style="left:304px;top:228px;width:287px"><div class="ic"><svg width="12" height="12" viewBox="0 0 12 12" fill="var(--blue)"><path d="M2 0 L5 3 L3.5 5 C4.5 7 5 7.5 7 8.5 L9 7 L12 10 L10 12 C5 12 0 7 0 2Z"/></svg></div><span class="lbl">Your Phone*</span></div>
  <div class="field" style="left:608px;top:228px;width:287px"><div class="ic"><svg width="13" height="10" viewBox="0 0 13 10" fill="var(--blue)"><path d="M0 0 H13 L6.5 5Z M0 2 L6.5 7 L13 2 V10 H0Z"/></svg></div><span class="lbl">Your Email*</span></div>
  <div class="field" style="left:304px;top:283px;width:591px;height:81px"><div class="ic" style="height:38px"><svg width="14" height="11" viewBox="0 0 14 11" fill="var(--blue)"><ellipse cx="5" cy="4" rx="5" ry="4"/><ellipse cx="9.5" cy="6.5" rx="4.5" ry="3.6"/></svg></div><span class="lbl">Your Message</span></div>

  <div class="btn-solid" style="left:534px;top:400px;width:131px;height:39px;background:var(--blue-soft);border-radius:0">SUBMIT NOW</div>
</section>

<footer class="site-footer">
  <svg class="abs" style="left:0;top:0" width="1200" height="378">
    <polygon points="0,38 95,110 0,235" fill="var(--blue)"/>
    <polygon points="1200,260 1200,378 1060,378" fill="var(--blue)"/>
  </svg>
  <div class="abs" style="left:500px;top:96px;width:200px;text-align:center;color:#fff">
    <div class="brand-name">CRESTLINE WEALTH</div>
    <div class="brand-sub" style="color:#c8cde0">MANAGEMENT</div>
  </div>
  <span class="f-nav" style="left:239px">HOME</span>
  <span class="f-nav" style="left:309px">ABOUT US</span>
  <span class="f-nav" style="left:405px">SERVICES</span>
  <span class="f-nav" style="left:498px">OUR TEAM</span>
  <span class="f-nav" style="left:596px">CONTACT US</span>
  <span class="f-nav" style="left:710px">PRIVACY POLICY</span>
  <span class="f-nav" style="left:846px">TERMS OF SERVICE</span>

  <div class="f-diamond" style="left:166px;top:226px"></div>
  <div class="f-diamond" style="left:462px;top:226px"></div>
  <div class="f-diamond" style="left:812px;top:226px"></div>
  <svg class="abs" style="left:177px;top:239px" width="16" height="12" viewBox="0 0 16 12" fill="#fff"><path d="M0 0 H16 L8 6Z M0 2 L8 8 L16 2 V12 H0Z"/></svg>
  <svg class="abs" style="left:475px;top:236px" width="12" height="17" viewBox="0 0 12 17" fill="#fff"><path d="M6 0 C2.5 0 0 2.6 0 6 C0 10 6 17 6 17 C6 17 12 10 12 6 C12 2.6 9.5 0 6 0Z M6 3.5 A2.5 2.5 0 1 1 6 8.5 A2.5 2.5 0 1 1 6 3.5Z" fill-rule="evenodd"/></svg>
  <svg class="abs" style="left:824px;top:238px" width="14" height="14" viewBox="0 0 12 12" fill="#fff"><path d="M2 0 L5 3 L3.5 5 C4.5 7 5 7.5 7 8.5 L9 7 L12 10 L10 12 C5 12 0 7 0 2Z"/></svg>

  <div class="f-label" style="left:229px;top:226px">EMAIL</div>
  <div class="f-value" style="left:229px;top:245px">info@crestlinewealth.com</div>
  <div class="f-label" style="left:523px;top:226px">ADDRESS</div>
  <div class="f-value" style="left:523px;top:245px">48 Harbor Lane, Fairview, OH 43210</div>
  <div class="f-label" style="left:873px;top:226px">PHONE</div>
  <div class="f-value" style="left:873px;top:245px;font-size:14px">(555) 201 4470</div>

  <div class="abs" style="left:142px;top:309px;width:916px;height:1px;background:#2e3275"></div>
  <div class="abs" style="left:142px;top:338px;font-size:11px;color:#fff">© 2024 CRESTLINE WEALTH. All Rights Reserved.</div>
  <div class="social" style="left:917px"></div>
  <div class="social" style="left:954px"></div>
  <div class="social" style="left:992px"></div>
  <div class="social" style="left:1030px"></div>
</footer>

</body>
</html>
```